Film Project Needs Investment Proposal

I'm trying to raise money to produce a feature film. I have the original mockup and the latest mockup uploaded to help show what I'm looking for. I've included the text and the images that should be used. Looking for a more professional and dynamic look to the pitch to project an impressive opportunity that can't refuse. Hopefully this will be fairly straightforward. I would love to have the elephant that was created as a iconic image to represent the movie. You can find that in the power point file. Thanks!

Industry/Entity Type

Investment

Requirements
Must have
• The text I have uploaded. It should follow the text. I have specific headers for each section of the text which I would like to see. These might be altered.
Nice to have
• Resemble the structure of the existing mockup brochures. 8-12 pages. Use the elephant logo that appears in the existing mockups-----a composite elephant image incorporating elements from the movie.
Should not have
• Cuts to the text.

```html
<!DOCTYPE html>
<html lang="en">
<head>
<meta charset="utf-8">
<title>Outlook – Investment Brochure Spread</title>
<link rel="stylesheet" href="https://fonts.googleapis.com/css2?family=Montserrat:wght@400;900&display=swap">
<style>
  :root {
    --canvas: #ffffff;
    --panel-black: #0e0e0e;
    --panel-grain: #2b2b2b;
    --text-light: #d4d4d4;
    --heading: #ffffff;
    --sky-top: #9fb1bd;
    --sky-low: #d7dcd6;
    --horizon: #c9b77a;
    --hide: #6e5a43;
    --hide-dark: #3f3327;
    --grass: #7c7838;
    --grass-dark: #4d4a22;
    --archive-light: #cdbd78;
    --archive: #9c8c4c;
    --archive-dark: #5e5430;
    --theatre: #2e2427;
    --theatre-mid: #5a4548;
    --projector: #f3e6c0;
    --gutter: rgba(0,0,0,0.22);
  }
  * { box-sizing: border-box; margin: 0; padding: 0; }
  html, body { width: 1200px; height: 1200px; overflow: hidden; background: var(--canvas); }

  .spread {
    position: absolute; left: 40px; top: 370px;
    width: 1120px; height: 460px;
    display: flex;
    box-shadow: 0 8px 22px rgba(0,0,0,0.16);
  }
  .spread::after {
    content: ""; position: absolute; left: 560px; top: 0; width: 2px; height: 100%;
    background: linear-gradient(90deg, transparent, var(--gutter), transparent);
  }

  .outlook-panel {
    width: 220px; height: 100%; flex: none;
    background: radial-gradient(circle at 35% 35%, var(--panel-grain), var(--panel-black) 72%);
    padding: 112px 16px 18px 20px;
    color: var(--text-light);
    font-family: "Montserrat", sans-serif;
  }
  .outlook-title {
    font-weight: 900; font-size: 28px; letter-spacing: 1px; line-height: 1;
    color: var(--heading); margin-bottom: 14px;
  }
  .outlook-list { list-style: disc; padding-left: 10px; }
  .outlook-list li { font-size: 9px; line-height: 12.5px; font-weight: 400; }

  .hero-photo {
    width: 640px; height: 100%; flex: none;
    background:
      radial-gradient(ellipse 42% 62% at 48% 50%, var(--hide-dark) 0%, var(--hide) 45%, rgba(110,90,67,0) 100%),
      linear-gradient(180deg, var(--sky-top) 0%, var(--sky-low) 38%, var(--horizon) 50%, var(--grass) 66%, var(--grass-dark) 100%);
  }

  .side-photos { width: 260px; height: 100%; flex: none; display: flex; flex-direction: column; }
  .archive-photo {
    flex: 1;
    background: linear-gradient(135deg, var(--archive-light), var(--archive) 50%, var(--archive-dark));
  }
  .theatre-photo {
    flex: 1;
    background:
      radial-gradient(circle at 100% 70%, var(--projector) 0%, rgba(243,230,192,0) 35%),
      linear-gradient(180deg, var(--theatre-mid), var(--theatre));
  }
</style>
</head>
<body>
  <section class="spread">
    <div class="outlook-panel">
      <h2 class="outlook-title">OUTLOOK</h2>
      <ul class="outlook-list">
        <li>The budget of the movie ranges from $2.6 million dependent on talent. Production is slated for an early 2018 shoot, allowing for a potential World Premiere at the 2019 Summit Ridge Film Festival. Dale Renner's track record with Summit Ridge, coupled with the attention received by the high profile collaboration with Corvin Hale and Ostrander, will help set THE EDGE OF WANT AND DREAD for a well-publicized international premiere, an ideal acquisition and distribution worldwide. The low price and universal appeal of the movie's story point to strong box office with a clear path to potential investor return on investment, congruent with critical and commercial international success. The movie's themes, cast and filmmakers give producers a clear position for a run at the Golden Reel Awards.</li>
      </ul>
    </div>
    <div class="hero-photo" role="img" aria-label="Full-bleed composite photo of an African elephant facing forward, ears spread, standing in tall savanna grass under a pale sky"></div>
    <div class="side-photos">
      <div class="archive-photo" role="img" aria-label="Photo of metal shelves stacked with old film canisters"></div>
      <div class="theatre-photo" role="img" aria-label="Photo of rows of cinema seats lit by a projector beam"></div>
    </div>
  </section>
</body>
</html>
```